A Gallery type Web design

We are developing a Wordpress based website for a client that does design construction projects. E.g. Pools, Lobbies, Toilets, etc. The website will mainly be to showcase their past projects and the collections they have.
No programming required, we just need the designs!
A sample of what the client is looking for:
http://velmora.it/
Pages to include:
• Home – A nice slider design to showcase selected photos
• Main Category Template
• Sub Category Template
• About us
• Contact us
Example of their Main Categories and their Sub Categories:
Collections - Granite
- Marble
- Sculpture
Projects - Private
- Public
- Commercial
- Overseas
Installation - Vanity tops
- Hall areas
- Toilets
The Main Category is to show a sample and link the user to the respective Sub Categories. The Sub Categories are to showcase all the photos they have from the category. Please leave a little space to add some text or caption for the photo.
Designs need to be mobile responsive!
I've attached their logo and some sample photos to use for mock ups. Let me know if you have any questions!

```html
<!DOCTYPE html>
<html lang="en">
<head>
<meta charset="utf-8">
<title>Granitra – Home</title>
<link rel="stylesheet" href="https://fonts.googleapis.com/css2?family=Open+Sans:ital,wght@0,400;0,600;0,700;1,400&display=swap">
<style>
:root{
  --bg:#1b1b1b;
  --bg-tone:#262626;
  --panel:#2b2b2b;
  --panel-edge:#3a3a3a;
  --red:#e0141c;
  --red-dark:#a80d12;
  --text:#bdbdbd;
  --text-light:#f2f2f2;
  --nav:#4a4a4a;
  --nav-dark:#333;
}
*{margin:0;padding:0;box-sizing:border-box}
html,body{width:1147px;height:1200px;overflow:hidden}
body{
  position:relative;
  font-family:"Open Sans",Arial,sans-serif;
  color:var(--text);
  background:
    radial-gradient(ellipse at 50% 35%,#2e2e2e 0%,rgba(0,0,0,0) 60%),
    linear-gradient(180deg,var(--bg-tone),var(--bg) 60%,#151515);
}
.interior-backdrop{position:absolute;inset:0;opacity:.5;
  background:linear-gradient(90deg,#222 0%,#2c2c2c 20%,#1e1e1e 50%,#2c2c2c 80%,#222 100%)}
.brand{position:absolute;left:156px;top:48px;display:flex;align-items:center;gap:10px}
.brand-square{width:14px;height:14px;background:var(--red)}
.brand-name{font-weight:700;font-size:26px;letter-spacing:2px;color:var(--red)}
.main-nav{position:absolute;top:46px;left:0}
.nav-item{position:absolute;height:35px;line-height:35px;text-align:center;font-size:14px;
  letter-spacing:.5px;text-transform:uppercase;color:var(--text-light);border-radius:3px;
  background:linear-gradient(180deg,#5a5a5a,var(--nav-dark));box-shadow:0 2px 4px rgba(0,0,0,.6)}
.nav-item::after{content:"";position:absolute;left:50%;bottom:-8px;margin-left:-8px;
  border:8px solid transparent;border-bottom:0;border-top-color:var(--nav-dark)}
.nav-item.is-active{background:linear-gradient(180deg,#f2262d,var(--red-dark))}
.nav-item.is-active::after{border-top-color:var(--red-dark)}
.slider{position:absolute;left:152px;top:127px;width:843px;height:536px;background:#0c0c0c;
  border-radius:4px;box-shadow:0 0 18px rgba(0,0,0,.8)}
.slide-photo{position:absolute;left:10px;top:10px;width:825px;height:518px;
  background:linear-gradient(160deg,#b9b4ab 0%,#6e6a63 35%,#2c2a28 60%,#9a9a96 100%)}
.thumb-rail{position:absolute;left:653px;top:10px;width:182px;height:518px;background:rgba(30,30,30,.55)}
.thumb-rail svg{position:absolute;left:0;top:0}
.welcome-tab{position:absolute;left:169px;top:711px;width:298px;height:46px;background:var(--panel);
  border-radius:3px 3px 0 0;box-shadow:0 -2px 4px rgba(0,0,0,.4);padding:12px 14px;
  font-size:17px;letter-spacing:1px;color:var(--red);text-transform:uppercase}
.intro-panel{position:absolute;left:152px;top:757px;width:844px;height:211px;background:var(--panel);
  border-radius:3px;box-shadow:0 3px 8px rgba(0,0,0,.6);padding:24px 31px;font-size:12.4px;line-height:21px}
.intro-panel h2{font-size:13.6px;font-weight:600;color:var(--text-light);margin-top:10px;line-height:22px}
.read-more{position:absolute;left:894px;top:968px;width:80px;height:20px;background:var(--panel);
  border-radius:0 0 3px 3px;font-size:10.5px;font-style:italic;color:#8a8a8a;text-align:center;line-height:18px}
.contact-title{position:absolute;left:160px;top:999px;font-size:14px;font-weight:600;color:var(--text-light)}
.contact-line{position:absolute;font-size:11.5px;color:var(--text);line-height:16px;display:flex;align-items:flex-start;gap:10px}
.contact-line svg{flex:none}
.location-map{position:absolute;left:465px;top:1046px;width:302px;height:118px;border:3px solid #ddd;
  background:linear-gradient(135deg,#e9e6df,#d8d4cb)}
.social-links{position:absolute;left:822px;top:1046px;display:flex;gap:5px}
.social-links span{width:21px;height:21px;background:#4a4a4a;border:1px solid #5c5c5c}
.social-links span:first-child{background:#3b5a9a}
.footer-brand{position:absolute;left:842px;top:1104px;display:flex;align-items:center;gap:6px}
.footer-brand .brand-name{font-size:18px;letter-spacing:1px}
.footer-brand .brand-square{width:10px;height:10px}
.copyright{position:absolute;right:151px;top:1153px;font-size:10.5px;color:var(--text)}
</style>
</head>
<body>
<div class="interior-backdrop" role="img" aria-label="Dimmed interior room photographs tiled as backdrop"></div>

<header>
  <div class="brand"><span class="brand-square"></span><span class="brand-name">GRANITRA</span></div>
  <nav class="main-nav">
    <a class="nav-item is-active" style="left:542px;width:70px">Home</a>
    <a class="nav-item" style="left:630px;width:110px">About us</a>
    <a class="nav-item" style="left:757px;width:112px">Category</a>
    <a class="nav-item" style="left:888px;width:104px">Contact</a>
  </nav>
</header>

<section class="slider">
  <div class="slide-photo" role="img" aria-label="Dining room and hallway with black and white hexagon mosaic floor"></div>
  <div class="thumb-rail">
    <svg width="182" height="518" viewBox="0 0 182 518">
      <defs>
        <linearGradient id="thumbFill" x1="0" y1="0" x2="0" y2="1">
          <stop offset="0" stop-color="#9a9a9a"/><stop offset="1" stop-color="#3c3c3c"/>
        </linearGradient>
      </defs>
      <polyline points="74,20 88,10 102,20" fill="none" stroke="#ddd" stroke-width="2"/>
      <polyline points="74,488 88,498 102,488" fill="none" stroke="#ddd" stroke-width="2"/>
      <g fill="url(#thumbFill)" stroke="#d5d5d5" stroke-width="3">
        <circle cx="88" cy="83" r="55" role="img" aria-label="Living room thumbnail"/>
        <circle cx="88" cy="153" r="55"/>
        <circle cx="88" cy="367" r="55"/>
        <circle cx="88" cy="410" r="55"/>
        <circle cx="88" cy="450" r="55"/>
      </g>
      <path d="M30,222 L16,232 L30,242 Z" fill="var(--red)"/>
      <circle cx="88" cy="222" r="60" fill="#8c8a86" stroke="#e0141c" stroke-width="4" role="img" aria-label="Selected slide thumbnail"/>
    </svg>
  </div>
</section>

<section>
  <h1 class="welcome-tab">Welcome to Granitra</h1>
  <div class="intro-panel">
    <p>Mr. Calvin Seow, the founder of Granitra Marketing Pte. Ltd. is a seasoned marketing professional, with over 27 years of sales and marketing management experience. He has a great understanding of the differing needs of building project requirements. Together with all supporting staffs, Granitra will strive to provide the best solution for you!</p>
    <h2>CORPORATE PROFILE OF GRANITRA MARKETING PTE. LTD.</h2>
    <p>Since incorporation, the management has positioned Granitra as an up-coming company, offering a wide range of services in the supply of exotic stones (marble and granite). Granitra also supplies a wide spectrum of products for the protection, restoration and maintenance of all stone surfaces before and after installation.</p>
  </div>
  <a class="read-more">Read More</a>
</section>

<footer>
  <h3 class="contact-title">GET IN TOUCH</h3>
  <div class="contact-line" style="left:161px;top:1042px">
    <svg width="22" height="20" viewBox="0 0 22 20"><path d="M11 2 L21 11 H18 V19 H13 V13 H9 V19 H4 V11 H1 Z" fill="#aaa"/></svg>
    <span>18 Marlow Crescent, #03-12 Harbourview Park,<br>Singapore 408812</span>
  </div>
  <div class="contact-line" style="left:164px;top:1103px">
    <svg width="18" height="18" viewBox="0 0 18 18"><path d="M4 1 L7 5 L5 7 Q7 11 11 13 L13 11 L17 14 L15 17 Q6 16 1 4 Z" fill="none" stroke="#aaa" stroke-width="1.5"/></svg>
    <span>656 410 2283</span>
  </div>
  <div class="contact-line" style="left:285px;top:1101px">
    <svg width="20" height="20" viewBox="0 0 20 20"><rect x="2" y="6" width="16" height="12" fill="none" stroke="#aaa" stroke-width="1.5"/><rect x="5" y="1" width="10" height="6" fill="none" stroke="#aaa" stroke-width="1.5"/></svg>
    <span>656 410 2290</span>
  </div>
  <div class="contact-line" style="left:161px;top:1150px">
    <svg width="18" height="14" viewBox="0 0 18 14"><rect x="1" y="1" width="16" height="12" fill="none" stroke="#aaa" stroke-width="1.5"/><polyline points="1,1 9,8 17,1" fill="none" stroke="#aaa" stroke-width="1.5"/></svg>
    <span>info@granitramktg.com</span>
  </div>
  <div class="location-map" role="img" aria-label="Street map showing the office location"></div>
  <div class="social-links"><span></span><span></span><span></span><span></span><span></span><span></span></div>
  <div class="footer-brand"><span class="brand-square"></span><span class="brand-name">GRANITRA</span></div>
  <p class="copyright">© 2014 Granitra. All rights Resverd</p>
</footer>
</body>
</html>
```